Homepage Design :) --- A website that connects Journalists to Sources to make brilliant news stories

I need a new homepage designed for a company based in California. The homepage is simple.
The website is BrightQuoteLink.com.

About us:
We are a platform that connects reporters to expert sources (normal people with specific expertise) so a reporter can quickly and easily source information for their news story. Also, the source gets cited in their major news article so it's a win-win situation.

Design:
We have no real slogan except maybe the slogan on the website (beautiful stories that connect us), though that can change too.

I would like to see designs of any style that you choose. We really only have one website color shown in blue on the website, you can use other colors in addition to that one or even change the theme color.

Attachments:
- Homepage to redesign, which you can go to the website yourself to check it out
- A mockup sketch of a revision idea that I had in mind with two people thinking short thoughts. Though this is just a random thought.... You can make anything you want! :)
- An image of what the logged in dashboard looks like just if you want a reference

The footer menu links will remain but can be anything color/style.

Make any ideas you want, keep the same amount of sections or add more, add any graphics or things that you want, etc. I want creativity to really attract customers the second they land on the page. A powerfully beautiful home page!

For reference, some competing websites are NewsWiseDesk.com, Vorlin.io, and plimsa.com
I noticed all these website use red/orange related colors, so maybe I should change the color theme to that? Again, your decision :)

```html
<!DOCTYPE html>
<html lang="en">
<head>
<meta charset="utf-8">
<title>BrightQuoteLink – Beautiful stories that connect us</title>
<link rel="stylesheet" href="https://fonts.googleapis.com/css2?family=Archivo:wght@300;400;600;700&display=swap">
<style>
  :root {
    --brand-orange: #f7941e;
    --ink: #111111;
    --paper: #ffffff;
    --canvas: #ffffff;
  }
  * { margin: 0; padding: 0; box-sizing: border-box; }
  html, body {
    width: 1200px;
    height: 900px;
    overflow: hidden;
    background: var(--canvas);
    font-family: "Archivo", Arial, sans-serif;
    color: var(--ink);
  }
  .site {
    position: absolute;
    left: 69px;
    top: 148px;
    width: 1081px;
    height: 597px;
    background: var(--paper);
    box-shadow: 0 0 4px rgba(0, 0, 0, 0.18);
  }

  /* header */
  .brand {
    position: absolute;
    left: 22px;
    top: 24px;
    font-weight: 700;
    color: var(--ink);
    text-align: center;
  }
  .brand-name { display: block; font-size: 24px; line-height: 26px; letter-spacing: 0.3px; }
  .brand-tagline { display: block; font-size: 7px; line-height: 10px; margin-top: 2px; }

  .nav {
    position: absolute;
    right: 22px;
    top: 15px;
    display: flex;
    align-items: center;
    gap: 15px;
  }
  .nav-link {
    font-size: 15px;
    font-weight: 600;
    color: var(--ink);
    text-decoration: none;
    margin-right: 1px;
  }
  .nav-button {
    display: flex;
    align-items: center;
    justify-content: center;
    width: 101px;
    height: 46px;
    border: 3px solid var(--brand-orange);
    border-radius: 23px;
    font-size: 15px;
    font-weight: 600;
    color: var(--ink);
    text-decoration: none;
  }

  /* hero */
  .hero-kicker {
    position: absolute;
    left: 0;
    width: 100%;
    top: 110px;
    text-align: center;
    font-size: 24px;
    font-weight: 600;
    letter-spacing: -0.3px;
  }
  .hero-title {
    position: absolute;
    left: 0;
    width: 100%;
    top: 137px;
    text-align: center;
    font-size: 67px;
    line-height: 80px;
    font-weight: 700;
    letter-spacing: -0.4px;
    white-space: nowrap;
    color: var(--brand-orange);
  }

  /* orange band */
  .intro-band {
    position: absolute;
    left: 0;
    top: 256px;
    width: 100%;
    height: 341px;
    background: var(--brand-orange);
    color: var(--paper);
  }
  .intro-points {
    position: absolute;
    left: 0;
    width: 100%;
    top: 40px;
    text-align: center;
    font-size: 22px;
    line-height: 30.5px;
    font-weight: 600;
    letter-spacing: -0.2px;
  }
  .intro-about {
    position: absolute;
    left: 0;
    width: 100%;
    top: 148px;
    text-align: center;
    font-size: 12px;
    line-height: 17px;
    font-weight: 300;
  }

  /* footer */
  .footer-col {
    position: absolute;
    top: 259px;
    font-size: 13px;
    line-height: 18.5px;
    color: var(--ink);
  }
  .footer-col h3 { font-size: 13px; font-weight: 700; line-height: 18px; margin-bottom: 0; }
  .footer-col a { display: block; color: var(--ink); text-decoration: none; font-weight: 400; }
  .footer-about { left: 22px; }
  .footer-info { left: 198px; top: 260px; }
  .footer-rules { left: 395px; top: 260px; }
</style>
</head>
<body>
  <main class="site">
    <header>
      <div class="brand">
        <span class="brand-name">BQL</span>
        <span class="brand-tagline">Bright Quote Link Service</span>
      </div>
      <nav class="nav">
        <a class="nav-link" href="#">How it works</a>
        <a class="nav-button" href="#">Sign Up</a>
        <a class="nav-button" href="#">Login</a>
      </nav>
    </header>

    <section class="hero">
      <p class="hero-kicker">Experience inspiring reporting</p>
      <h1 class="hero-title">Beautiful stories that connect us</h1>
    </section>

    <section class="intro-band">
      <p class="intro-points">
        Find sources for the stories that you need information.<br>
        Browse profiles of your sources to verify expertise.<br>
        Explore pitches to discover new topics.
      </p>
      <p class="intro-about">
        Bright Quote Link (BQL) connects reporters and sources from around the world.<br>
        You want the real, honest stories. We connect you to the experts.
      </p>

      <footer>
        <div class="footer-col footer-about">
          <h3>About</h3>
          <a href="#">Contact us</a>
          <a href="#">How it works</a>
          <a href="#">Job Board</a>
        </div>
        <div class="footer-col footer-info">
          <h3>Information</h3>
          <a href="#">Terms of Service</a>
          <a href="#">Privacy Policy</a>
        </div>
        <div class="footer-col footer-rules">
          <h3>Rules</h3>
          <a href="#">Reporter &amp; Source Rules</a>
          <a href="#">Refund Policy</a>
        </div>
      </footer>
    </section>
  </main>
</body>
</html>
```